Real Estate Acquisition Company Needs Business Card Design

Tellwyn Real Estate is in need of a business card design!

As a Real Estate Acquisition Company, Tellwyn Real Estate conducts mutually beneficial real estate transactions that actively consider the needs of the seller. At Tellwyn Real Estate we’re actively buying properties from those that see value in a direct transaction, but more importantly want reassurances that they, personally, are in integral part of it. Of course, it all starts with fair market value, but it doesn’t stop there. We’ve found the most success when we offer more. And with our deep experience in this industry, we’ve discovered that we have a lot to offer!

We already have a logo and brand guidelines that we've uploaded. Our final design should stay true to the guidelines. We are looking for a business card design that has two names (Ex. Jane Doe & John Doe) and contact information for each person- this way the company principals can share a card as they often do business as a team.
Updates

The criteria was unfortunately not met on most designs. We are looking for a card that has a layout for TWO names and respective contact information for each of the two people. Almost all designs only had a space for one name and one set of contact information.

Industry/Entity Type

Real Estate

Contact Information for Business Card

We are looking for a business card design that has two names (Ex. Jane Doe & John Doe) and each of their contact information- this way the company principals can share a card as they often do business as a team.

Font styles to use
Other font styles liked:
• Use Brand Guidelines

Requirements
Must have
• Please stay true to our Brand Guidelines for colours, fonts, and positioning of logo.

We require a layout for two names and respective contact information. The company principals work as a team and want a card that has both their information on it.

```html
<!DOCTYPE html>
<html lang="en">
<head>
<meta charset="utf-8">
<title>Tellwyn Real Estate – Business Card</title>
<link href="https://fonts.googleapis.com/css2?family=Montserrat:wght@500;600;700&family=Open+Sans:wght@400;600&display=swap" rel="stylesheet">
<style>
  :root{
    --navy:#15213a;
    --gold:#f0b03c;
    --white:#ffffff;
    --backdrop:#2b2d31;
    --ink:#15213a;
  }
  *{margin:0;padding:0;box-sizing:border-box;}
  html,body{width:1200px;height:900px;overflow:hidden;}
  body{background:var(--backdrop);position:relative;font-family:"Open Sans",sans-serif;}

  .card{position:absolute;left:267px;width:665px;height:380px;overflow:hidden;border-radius:2px;}
  .card-front{top:45px;background:var(--white);}
  .card-back{top:470px;background:var(--navy);display:flex;align-items:center;justify-content:center;}

  .card-shapes{position:absolute;inset:0;}

  .brand-name{font-family:"Montserrat",sans-serif;font-weight:600;letter-spacing:2px;text-transform:uppercase;white-space:nowrap;}
  .card-front .brand-name{position:absolute;right:40px;top:52px;font-size:30px;color:var(--ink);}
  .card-back .brand-name{font-size:40px;color:var(--white);}

  .contact{position:absolute;top:168px;width:270px;color:var(--white);}
  .contact-left{left:40px;}
  .contact-right{left:372px;}
  .contact-name{font-family:"Montserrat",sans-serif;font-weight:700;font-size:17px;letter-spacing:1px;text-transform:uppercase;}
  .contact-title{font-size:14px;color:var(--gold);margin-bottom:12px;}
  .contact-line{display:flex;align-items:center;gap:10px;font-size:13.5px;margin-top:7px;white-space:nowrap;}
  .icon-box{width:26px;height:26px;border:1.6px solid var(--gold);border-radius:6px;display:flex;align-items:center;justify-content:center;flex:none;}

  .website{position:absolute;left:70px;top:326px;font-size:17px;font-weight:600;color:var(--ink);letter-spacing:.3px;}
</style>
</head>
<body>

<section class="card card-front" aria-label="Business card front">
  <svg class="card-shapes" width="665" height="380" viewBox="0 0 665 380">
    <polygon points="0,128 665,152 665,292 0,300" fill="var(--navy)"/>
    <line x1="0" y1="126" x2="665" y2="150" stroke="var(--gold)" stroke-width="2.5"/>
    <line x1="352" y1="170" x2="332" y2="282" stroke="var(--gold)" stroke-width="1.2"/>
    <polygon points="505,292 665,292 665,380 480,380" fill="var(--gold)"/>
  </svg>

  <div class="brand-name">Tellwyn Real Estate</div>

  <div class="contact contact-left">
    <div class="contact-name">Rowan Hale</div>
    <div class="contact-title">Director and ceo</div>
    <div class="contact-line">
      <span class="icon-box"><svg width="14" height="14" viewBox="0 0 24 24"><path d="M6.6 10.8a15 15 0 0 0 6.6 6.6l2.2-2.2c.3-.3.7-.4 1-.2 1.1.4 2.3.6 3.6.6.6 0 1 .4 1 1V20c0 .6-.4 1-1 1A17 17 0 0 1 3 4c0-.6.4-1 1-1h3.5c.6 0 1 .4 1 1 0 1.3.2 2.5.6 3.6.1.3 0 .7-.2 1z" fill="var(--white)"/></svg></span>
      +1 555 014 2290
    </div>
    <div class="contact-line">
      <span class="icon-box"><svg width="14" height="12" viewBox="0 0 24 18"><rect x="1" y="1" width="22" height="16" rx="1.5" fill="var(--white)"/><path d="M1 2l11 8 11-8" stroke="var(--navy)" stroke-width="2" fill="none"/></svg></span>
      rowan@tellwynrealestate.ca
    </div>
  </div>

  <div class="contact contact-right">
    <div class="contact-name">Elena Marsh</div>
    <div class="contact-title">Director and coo</div>
    <div class="contact-line">
      <span class="icon-box"><svg width="14" height="14" viewBox="0 0 24 24"><path d="M6.6 10.8a15 15 0 0 0 6.6 6.6l2.2-2.2c.3-.3.7-.4 1-.2 1.1.4 2.3.6 3.6.6.6 0 1 .4 1 1V20c0 .6-.4 1-1 1A17 17 0 0 1 3 4c0-.6.4-1 1-1h3.5c.6 0 1 .4 1 1 0 1.3.2 2.5.6 3.6.1.3 0 .7-.2 1z" fill="var(--white)"/></svg></span>
      +1 555 014 3317
    </div>
    <div class="contact-line">
      <span class="icon-box"><svg width="14" height="12" viewBox="0 0 24 18"><rect x="1" y="1" width="22" height="16" rx="1.5" fill="var(--white)"/><path d="M1 2l11 8 11-8" stroke="var(--navy)" stroke-width="2" fill="none"/></svg></span>
      elena@tellwynrealestate.ca
    </div>
  </div>

  <div class="website">www.tellwynrealestate.ca</div>
</section>

<section class="card card-back" aria-label="Business card back">
  <div class="brand-name">Tellwyn Real Estate</div>
</section>

</body>
</html>
```